Tumbleleaf Snacks Website redesign

I would like a redesign of my current website, www.tumbleleafsnacks.example. We make a pre-popped and packaged popcorn that we sell to grocers, retailers, and on-line. My current website is not appealing, and I would like to attract more customers to my online store. Our competition is Lofty Crunch, Brightbite, and Zing Zang Puff to name a few, please take a look at their sites for examples. What sets Tumbleleaf apart from competitors is our 3 ingredients, non-GMO WHITE popcorn, corn oil, kosher salt. White kernels pop up more tender and virtually hull-less with a sweet corn flavor. Tumbleleaf is all-natural, kosher, and nothing artificial.

Coding

```html
<!DOCTYPE html>
<html lang="en">
<head>
<meta charset="utf-8">
<title>Tumbleleaf Snacks</title>
<link href="https://fonts.googleapis.com/css2?family=Paytone+One&family=Inter:wght@400;500;600;700&display=swap" rel="stylesheet">
<style>
:root{
  --stage:#b185fb;
  --frame:#ffffff;
  --violet:#7420fb;
  --orange:#fd6c32;
  --mint:#92f4a8;
  --pink:#f57df0;
  --mist:#f1f1f5;
  --ink:#3b2a1f;
  --black:#111111;
  --white:#ffffff;
}
*{box-sizing:border-box;margin:0;padding:0}
html,body{width:1200px;height:1200px;overflow:hidden}
body{background:var(--stage);font-family:"Inter",sans-serif;position:relative}
.display{font-family:"Paytone One",sans-serif;font-weight:400}
.frame{position:absolute;left:350px;top:24px;width:500px;height:1152px;background:var(--frame);border-radius:10px}
.panel{position:absolute;border-radius:5px;overflow:hidden}
.center{display:flex;flex-direction:column;align-items:center;text-align:center}

.hero{left:356px;top:30px;width:487px;height:200px;background:var(--violet)}
.nav{position:absolute;left:6px;top:6px;width:475px;height:16px;background:var(--white);border-radius:8px;display:flex;align-items:center;padding:0 7px}
.brand{font-size:5px;font-weight:700;color:var(--violet);display:flex;align-items:center;gap:3px}
.brand-dot{width:8px;height:8px;border-radius:50%;background:#f5a623}
.nav-links{margin-left:auto;display:flex;align-items:center;gap:6px;font-size:4.4px;color:var(--black)}
.nav-links .active{font-weight:700}
.nav-icon{width:8px;height:8px;border-radius:50%;background:var(--black)}
.hero-copy{position:absolute;left:0;right:0;top:45px}
.hero h1{color:var(--white);font-size:21px;line-height:25px}
.hero p{color:var(--white);font-size:6.2px;line-height:9.5px;margin-top:8px}
.btn{display:inline-block;font-weight:600;color:var(--white);border-radius:2px;box-shadow:0 1px 2px rgba(0,0,0,.25)}
.btn-orange{background:var(--orange);font-size:6.2px;padding:4px 5px;margin-top:12px}
.btn-violet{background:var(--violet);font-size:6.2px;padding:4px 5px}

.welcome{left:356px;top:237px;width:293px;height:200px;background:var(--orange)}
.welcome h2{color:var(--white);font-size:16px;margin-top:30px}
.welcome p{color:var(--white);font-size:6.2px;line-height:9.5px;margin-top:10px;padding:0 20px}
.welcome .btn-violet{margin-top:11px;position:relative;z-index:2}
.phone-art{position:absolute;left:66px;top:89px;width:106px;height:111px;border-radius:40px 40px 0 0;background:linear-gradient(150deg,#a34a1e,#4a1d0b)}

.featured{left:655px;top:237px;width:188px;height:200px;background:var(--mint)}
.featured .label{position:absolute;left:12px;top:11px;font-size:8px;color:var(--violet)}
.bag{background:linear-gradient(160deg,#ffffff,#e8e3dd);border-radius:3px}
.featured .bag{position:absolute;left:52px;top:34px;width:82px;height:118px}
.featured .name{position:absolute;left:0;right:0;top:165px;font-size:10px;color:var(--ink)}
.featured .price{position:absolute;left:0;right:0;top:180px;font-size:8.6px;font-weight:600;color:var(--black)}

.sandiego{left:356px;top:444px;width:188px;height:200px;background:linear-gradient(180deg,#6c7c68 0%,#8a7a66 40%,#f4e98e 62%,#8ee8b0 75%,#5e2b2b 90%,#3a1e22 100%)}
.sandiego h3{position:absolute;left:0;right:0;top:45px;color:var(--white);font-size:20px;line-height:25px;text-align:center}

.promise{left:551px;top:444px;width:292px;height:200px;background:var(--violet)}
.promise h3{position:absolute;left:0;right:0;top:50px;color:var(--pink);font-size:20px;line-height:25px;text-align:center}
.kernels{position:absolute;left:36px;top:108px;width:212px;height:92px;border-radius:50%;background:radial-gradient(ellipse,rgba(226,200,240,.55),rgba(116,32,251,0) 70%)}

.products{left:356px;top:651px;width:487px;height:242px;background:var(--mist)}
.products h2{position:absolute;left:0;right:0;top:18px;text-align:center;color:var(--violet);font-size:21px}
.card{position:absolute;top:59px;width:153px;height:177px;background:var(--white);border-radius:4px}
.card .bag{position:absolute;left:36px;top:16px;width:82px;height:118px}
.card .title{position:absolute;left:9px;top:146px;font-size:7.5px;color:var(--ink)}
.card .sub{position:absolute;left:9px;top:160px;font-size:6px;color:var(--black)}
.card .tag{position:absolute;right:9px;top:154px;background:var(--mist);font-size:6.4px;font-weight:600;padding:2px 4px;border-radius:2px}
.shop-btn{position:absolute;left:428px;top:223px;display:flex;align-items:center;gap:4px}

.review{left:356px;top:900px;width:487px;height:131px;background:var(--mint)}
.review h2{color:var(--ink);font-size:15.5px;line-height:21px;margin-top:19px;padding:0 100px}
.review p{color:var(--ink);font-size:6.2px;line-height:9.5px;margin-top:10px;padding:0 120px}
.review .btn-violet{margin-top:11px}

.footer{left:356px;top:1038px;width:487px;height:131px;background:var(--violet)}
.footer h2{color:var(--white);font-size:21px;margin-top:31px}
.footer-links{display:flex;gap:7px;margin-top:10px;font-size:6.4px;color:var(--white)}
.footer-links .active{font-weight:700}
.footer-rule{position:absolute;left:6px;right:6px;top:113px;border-top:.6px solid rgba(255,255,255,.35)}
.copyright{position:absolute;left:0;right:0;top:118px;font-size:5.4px;color:var(--white);text-align:center}
</style>
</head>
<body>
<div class="frame"></div>

<section class="panel hero">
  <nav class="nav">
    <div class="brand"><span class="brand-dot"></span>Tumbleleaf</div>
    <div class="nav-links">
      <span class="active">Home</span><span>Shop</span><span>About Us</span><span>|</span>
      <span class="nav-icon"></span><span class="nav-icon" style="margin-left:-3px"></span>
    </div>
  </nav>
  <div class="hero-copy center">
    <h1 class="display">All-natural, Southern<br>California popcorn</h1>
    <p>Experience the perfect crunch made with just three pure ingredients.<br>No fluff, no fuss—just better popcorn.</p>
    <span class="btn btn-orange">Get Your Bag Today</span>
  </div>
</section>

<section class="panel welcome center">
  <h2 class="display">Welcome to Tumbleleaf Snacks</h2>
  <p>Popped and distributed in California! Please ask your local store to carry Tumbleleaf-<br>Thank you for your support!</p>
  <span class="btn btn-violet">(555) 014-2290</span>
  <div class="phone-art" role="img" aria-label="Illustration of a copper telephone handset"></div>
</section>

<section class="panel featured">
  <div class="label display">Featured Product</div>
  <div class="bag" role="img" aria-label="Photo of a clear bag of Tumbleleaf popcorn"></div>
  <div class="name display" style="text-align:center">Tumbleleaf Snacks, case of 6</div>
  <div class="price" style="text-align:center">$40.00</div>
</section>

<section class="panel sandiego" role="img" aria-label="Illustration of a sunset beach with palm trees">
  <h3 class="display">San Diego<br>Made</h3>
</section>

<section class="panel promise">
  <h3 class="display">No Preservatives.<br>Gluten Free.</h3>
  <div class="kernels" role="img" aria-label="Scattered popped popcorn kernels"></div>
</section>

<section class="panel products">
  <h2 class="display">All Products</h2>
  <article class="card" style="left:87px">
    <div class="bag" role="img" aria-label="Photo of a bag of Tumbleleaf popcorn"></div>
    <div class="title display">Tumbleleaf Snacks</div>
    <div class="sub">Case of 6</div>
    <div class="tag">$40.00</div>
  </article>
  <article class="card" style="left:247px">
    <div class="bag" role="img" aria-label="Photo of a bag of Tumbleleaf popcorn"></div>
    <div class="title display">Tumbleleaf Snacks</div>
    <div class="sub">Case of 15</div>
    <div class="tag">$65.00</div>
  </article>
  <span class="btn btn-violet shop-btn">Go to Shop
    <svg width="8" height="7" viewBox="0 0 8 7" aria-hidden="true"><path d="M0.5 2.5h7l-1 4h-5z" fill="none" stroke="#fff" stroke-width=".8"/><path d="M2.5 2.5l1.5-2 1.5 2" fill="none" stroke="#fff" stroke-width=".8"/></svg>
  </span>
</section>

<section class="panel review center">
  <h2 class="display">Better than #moviepopcorn, clean taste, quality corn</h2>
  <p>"Better than #moviepopcorn, clean taste, quality corn" - We love hearing reviews from our customers. Thanks for the support!</p>
  <span class="btn btn-violet">Contact Us</span>
</section>

<footer class="panel footer center">
  <h2 class="display">Tumbleleaf Snacks</h2>
  <div class="footer-links"><span class="active">Home</span><span>Shop</span><span>About Us</span></div>
  <div class="footer-rule"></div>
  <div class="copyright">Copyright © 2024 Tumbleleaf Snacks - All Rights Reserved.</div>
</footer>
</body>
</html>
```